Corvale Mechanical - Letterhead

We are a plumbing and hvac company based in Calgary. This letterhead will be on our quotes, invoices, preventative maintenance proposals etc.

```html
<!DOCTYPE html>
<html lang="en">
<head>
<meta charset="utf-8">
<title>Corvale Mechanical – Letterhead</title>
<link rel="stylesheet" href="https://fonts.googleapis.com/css2?family=Open+Sans:wght@400;700&family=Roboto:wght@400&display=swap">
<style>
  :root {
    --backdrop: #dedede;
    --paper: #fafafa;
    --ink: #4a4a4a;
    --brand-blue: #1c70b7;
    --orange-1: #e85424;
    --orange-2: #ee7b47;
    --orange-3: #f29a6d;
    --orange-4: #f4b691;
    --signature-tone: #f0f0f0;
  }
  * { box-sizing: border-box; margin: 0; padding: 0; }
  html, body {
    width: 1200px; height: 800px; overflow: hidden;
    background: var(--backdrop);
  }
  .canvas {
    width: 1200px; height: 800px;
    display: flex; align-items: center; justify-content: center;
  }
  .letterhead {
    position: relative;
    width: 556px; height: 776px;
    background: var(--paper);
    box-shadow: 0 6px 18px rgba(0,0,0,0.14);
    font-family: "Open Sans", sans-serif;
    color: var(--ink);
  }
  .brand {
    position: absolute; left: 50px; top: 66px;
    display: flex; align-items: center; gap: 8px;
    font-family: "Open Sans", sans-serif;
    font-weight: 700; font-size: 17px; letter-spacing: 0.5px;
    color: var(--brand-blue);
    text-transform: uppercase;
    line-height: 1.1;
  }
  .brand-dot {
    width: 14px; height: 14px; border-radius: 50%;
    background: var(--brand-blue); flex: none;
  }
  .contact {
    position: absolute; left: 372px; top: 55px;
    border-left: 1.5px solid var(--brand-blue);
    padding-left: 14px;
    font-family: "Roboto", sans-serif;
    font-style: normal;
    font-size: 9.6px; line-height: 12.6px;
    color: var(--ink);
  }
  .contact .address { margin-bottom: 2px; }
  .contact-line { display: flex; align-items: center; gap: 4px; }
  .contact-line svg { width: 8px; height: 8px; flex: none; }
  .letter-body {
    position: absolute; left: 50px; top: 180px; width: 456px;
    font-size: 10.3px; line-height: 15px;
  }
  .letter-body p { margin-bottom: 15px; text-align: justify; }
  .letter-body .salutation, .letter-body .closing { text-align: left; margin-bottom: 0; }
  .letter-body .salutation { margin-bottom: 15px; }
  .signature-area {
    position: absolute; left: 50px; top: 574px;
    width: 66px; height: 62px;
  }
  .footer-band {
    position: absolute; left: 0; bottom: 0; width: 100%; height: 23px;
    display: flex;
  }
  .footer-band .band-blue { flex: 0 0 67.4%; background: var(--brand-blue); }
  .footer-band .band-orange { flex: 1; }
  .band-orange.o1 { background: var(--orange-1); }
  .band-orange.o2 { background: var(--orange-2); }
  .band-orange.o3 { background: var(--orange-3); }
  .band-orange.o4 { background: var(--orange-4); }
</style>
</head>
<body>
<div class="canvas">
  <article class="letterhead">
    <header>
      <div class="brand"><span class="brand-dot"></span><span>Corvale<br>Mechanical</span></div>
      <address class="contact">
        <div class="address">1820 Bowridge Drive,<br>Suite 210 Calgary.</div>
        <div class="contact-line">
          <svg viewBox="0 0 10 10"><path d="M1 4 Q5 0 9 4 L8 5 L6.5 4 L6.5 3 Q5 2.5 3.5 3 L3.5 4 L2 5 Z M2.5 5.5 H7.5 V9 H2.5 Z" fill="var(--orange-1)"/></svg>
          <span>403.555.0172</span>
        </div>
        <div class="contact-line">
          <svg viewBox="0 0 10 10"><rect x="0.5" y="2" width="9" height="6.5" fill="var(--orange-1)"/><path d="M0.8 2.3 L5 5.6 L9.2 2.3" stroke="#fff" stroke-width="0.9" fill="none"/></svg>
          <span>info@corvalemech.ca</span>
        </div>
        <div class="contact-line">
          <svg viewBox="0 0 10 10"><circle cx="5" cy="5" r="4.5" fill="var(--orange-1)"/><path d="M3 2.5 Q4.5 3.5 4 5 Q6 5.5 5.5 7.5 M6.5 2 Q7 3.5 8.5 3.8" stroke="#fff" stroke-width="0.9" fill="none"/></svg>
          <span>www.corvalemech.ca</span>
        </div>
      </address>
    </header>

    <section class="letter-body">
      <p class="salutation">Dear customer,</p>
      <p>Lorem ipsum dolor sit amet, consectetur adipisicing elit, sed do eiusmod tempor incididunt ut labore et dolore magna aliqua. Ut enim ad minim veniam, quis nostrud exercitation ullamco laboris nisi ut aliquip ex ea commodo consequat. Duis aute irure dolor in reprehenderit in voluptate velit esse cillum dolore eu fugiat nulla pariatur. Excepteur sint occaecat cupidatat non proident, sunt in culpa qui officia deserunt mollit anim id est laborum.</p>
      <p>Lorem ipsum dolor sit amet, consectetur adipisicing elit, sed do eiusmod tempor incididunt ut labore et dolore magna aliqua. Ut enim ad minim veniam, quis nostrud exercitation ullamco laboris nisi ut aliquip ex ea commodo consequat. Duis aute irure dolor in reprehenderit in voluptate velit esse cillum dolore eu fugiat nulla pariatur. Excepteur sint occaecat cupidatat non proident, sunt in culpa qui officia deserunt mollit anim id est laborum.</p>
      <p>Lorem ipsum dolor sit amet, consectetur adipisicing elit, sed do eiusmod tempor incididunt ut labore et dolore magna aliqua. Ut enim ad minim veniam, quis nostrud exercitation ullamco laboris nisi ut aliquip ex ea commodo consequat. Duis aute irure dolor in reprehenderit in voluptate velit esse cillum dolore eu fugiat nulla pariatur. Excepteur sint occaecat cupidatat non proident, sunt in culpa qui officia deserunt mollit anim id est laborum.</p>
      <p>Lorem ipsum dolor sit amet, consectetur adipisicing elit, sed do eiusmod tempor incididunt ut labore et dolore magna aliqua. Ut enim ad minim veniam, quis nostrud exercitation ullamco laboris nisi ut aliquip ex ea commodo consequat. Duis aute irure dolor in reprehenderit.</p>
      <p class="closing">Yours Sincerely,</p>
    </section>

    <svg class="signature-area" viewBox="0 0 66 62" role="img" aria-label="Handwritten signature of the sender">
      <rect width="66" height="62" rx="3" fill="var(--signature-tone)"/>
    </svg>

    <footer class="footer-band">
      <div class="band-blue"></div>
      <div class="band-orange o1"></div>
      <div class="band-orange o2"></div>
      <div class="band-orange o3"></div>
      <div class="band-orange o4"></div>
    </footer>
  </article>
</div>
</body>
</html>
```